Skincare Line needs a label design

I need a label design for a new company based on Vancouver Island, Canada called 'Velora Brisk" We have formulated a skincare line for those with hyperpigmentation (sunspots, age spots, freckles etc) and also for those wanting to reduce redness caused from acne, rosacea, eczema, psoriasis and other skin conditions. We would like to see designs that use earth based colors as we have used microgreens as our inspiration and they come in all sorts of colors from deep greens to fuscia pink and bright yet deep yellows, Maroons, and purples are also quite common in these tiny plants. The final design should communicate high-end, classy yet effective ingredients.

Target Market(s)

Those with skin conditions such as eczema, acne rosacea and hyperpigmentation (sun spots, age spots, discoloration)

Industry/Entity Type

skincare line such as Cleanser, Toner, Serum, eye cream, facial cream

Logo Text

Velora Brisk

Requirements
Must have
• Size of label is 1.914inches x 5.3835 inches
Nice to have
• nice to see color. I also like the microgreen I uploaded but it's not necessary.

```html
<!DOCTYPE html>
<html lang="en">
<head>
<meta charset="utf-8">
<title>Velora Brisk — Microgreens Serum Label</title>
<link rel="stylesheet" href="https://fonts.googleapis.com/css2?family=Playfair+Display:wght@400;500&family=Source+Serif+4:opsz,wght@8..60,400;8..60,500&display=swap">
<style>
  :root {
    --backdrop: #f4f5f5;
    --label: #ffffff;
    --ink: #2b2d2e;
    --ink-soft: #3a3c3d;
    --green: #8db44a;
    --green-light: #a9c97a;
    --green-band: #8fb74e;
    --band-text: #f3f8ea;
  }
  * { margin: 0; padding: 0; box-sizing: border-box; }
  html, body {
    width: 1200px;
    height: 1200px;
    overflow: hidden;
    background: var(--backdrop);
  }
  .canvas {
    position: relative;
    width: 1200px;
    height: 1200px;
    display: flex;
    align-items: center;
    justify-content: center;
  }
  .label {
    position: relative;
    width: 580px;
    height: 1000px;
    background: var(--label);
    box-shadow: 0 2px 14px rgba(0,0,0,0.06);
    overflow: hidden;
  }
  .brand {
    position: absolute;
    left: 66px;
    top: 280px;
    display: flex;
    align-items: center;
    gap: 16px;
  }
  .brand-dot {
    width: 14px;
    height: 14px;
    border-radius: 50%;
    background: var(--ink);
    flex: none;
  }
  .brand-name {
    font-family: 'Playfair Display', serif;
    font-weight: 400;
    font-size: 32px;
    letter-spacing: 0.18em;
    text-transform: uppercase;
    color: var(--ink);
    white-space: nowrap;
  }
  .product-title {
    position: absolute;
    left: 66px;
    top: 560px;
    font-family: 'Playfair Display', serif;
    font-weight: 500;
    font-size: 116px;
    line-height: 1;
    color: var(--ink);
    letter-spacing: -0.01em;
  }
  .product-line {
    position: absolute;
    left: 70px;
    top: 728px;
    font-family: 'Source Serif 4', serif;
    font-weight: 500;
    font-size: 40px;
    line-height: 1;
    letter-spacing: 0.09em;
    color: var(--green);
  }
  .sprout-accent {
    position: absolute;
    left: 486px;
    top: 700px;
    width: 94px;
    height: 66px;
    background: linear-gradient(135deg, rgba(141,180,74,0.03), rgba(141,180,74,0.18));
  }
  .benefit-band {
    position: absolute;
    left: 66px;
    right: 0;
    top: 774px;
    height: 98px;
    background: linear-gradient(90deg, var(--green-light), var(--green-band));
    padding: 10px 8px 0 10px;
  }
  .benefit-band p {
    font-family: 'Source Serif 4', serif;
    font-size: 25px;
    line-height: 0.98;
    color: var(--band-text);
    letter-spacing: -0.02em;
    white-space: nowrap;
  }
  .net-content {
    position: absolute;
    left: 68px;
    top: 900px;
    font-family: 'Source Serif 4', serif;
    font-size: 30px;
    color: var(--ink-soft);
  }
</style>
</head>
<body>
  <main class="canvas">
    <section class="label">
      <div class="brand">
        <span class="brand-dot"></span>
        <span class="brand-name">Velora Brisk</span>
      </div>

      <h1 class="product-title">SERUM</h1>
      <h2 class="product-line">MICROGREENS</h2>
      <div class="sprout-accent" role="img" aria-label="Line drawing of microgreen sprouts"></div>

      <div class="benefit-band">
        <p>reduce redness caused from<br>acne, rosacea, eczema, psoriasis and<br>other skin conditions</p>
      </div>

      <p class="net-content">Net Weight 30 ml</p>
    </section>
  </main>
</body>
</html>
```